TVM8 Business Card Design Project

Design which catches the client with the first impression. A design which is professional and classy with elegance. We have also got another project running and the winning prize for that is $240 "tvm8 print + graphic design".
For all the company details please visit www.tvm8.com.
Please find the logo attached and i would like to have good colors for my business card.
, Design which catches the client with the first impression. A design which is professional and classy with elegance.
TVM8 is running two projects at the same time, please feel free to participate. The other project name is
Business

```html
<!DOCTYPE html>
<html lang="en">
<head>
<meta charset="utf-8">
<title>TVM8 Business Card</title>
<link rel="stylesheet" href="https://fonts.googleapis.com/css2?family=Roboto+Slab:wght@400;700&display=swap">
<style>
  :root {
    --backdrop: #d9d9db;
    --card-green: #3db383;
    --lime: #9dcb3a;
    --ink: #0b0b0b;
    --teal: #3db383;
    --social: #2f6fb6;
  }
  html, body {
    margin: 0;
    padding: 0;
    width: 1200px;
    height: 900px;
    overflow: hidden;
    background: var(--backdrop);
    font-family: "Roboto Slab", serif;
  }
  .canvas {
    position: relative;
    width: 1200px;
    height: 900px;
  }
  .card {
    position: absolute;
    left: 320px;
    width: 560px;
    height: 320px;
    border-radius: 22px;
    overflow: hidden;
    box-shadow: 0 6px 18px rgba(0,0,0,0.18);
  }
  .card-back {
    top: 100px;
    background: var(--card-green);
  }
  .card-front {
    top: 470px;
    background: var(--lime);
  }
  .back-brand {
    position: absolute;
    left: 50px;
    bottom: 48px;
    color: var(--ink);
  }
  .brand-name {
    font-weight: 700;
    font-size: 64px;
    line-height: 1;
    letter-spacing: 2px;
    display: flex;
    align-items: center;
    gap: 14px;
  }
  .brand-dot {
    width: 34px;
    height: 34px;
    border-radius: 50%;
    background: currentColor;
  }
  .back-url {
    margin-top: 10px;
    font-size: 13px;
    letter-spacing: 9px;
  }
  .front-shape {
    position: absolute;
    inset: 0;
  }
  .front-brand {
    position: absolute;
    left: 255px;
    top: 26px;
    color: var(--teal);
  }
  .front-brand .brand-name { font-size: 54px; }
  .front-brand .brand-dot { width: 30px; height: 30px; }
  .social {
    position: absolute;
    left: 72px;
    top: 110px;
    display: flex;
    gap: 6px;
  }
  .social span {
    width: 20px;
    height: 20px;
    border-radius: 3px;
    background: var(--social);
  }
  .contact {
    position: absolute;
    color: var(--ink);
    font-size: 14px;
    display: flex;
    align-items: center;
    gap: 6px;
  }
  .contact svg { width: 14px; height: 14px; }
  .person-name {
    position: absolute;
    left: 70px;
    top: 200px;
    font-weight: 700;
    font-size: 19px;
    color: var(--ink);
  }
  .person-role {
    position: absolute;
    left: 70px;
    top: 226px;
    font-size: 13px;
    color: var(--ink);
  }
  .contact-web { left: 350px; top: 178px; }
  .contact-mail { left: 200px; top: 222px; }
  .contact-phone { left: 70px; top: 270px; }
</style>
</head>
<body>
<main class="canvas">
  <section class="card card-back">
    <div class="back-brand">
      <div class="brand-name"><span class="brand-dot"></span>TVM8</div>
      <div class="back-url">www.tvm8.com</div>
    </div>
  </section>

  <section class="card card-front">
    <svg class="front-shape" viewBox="0 0 560 320" width="560" height="320" aria-hidden="true">
      <path d="M0,0 H560 V40 C530,120 420,128 300,128 C180,128 70,132 0,170 Z" fill="var(--ink)"/>
      <path d="M560,40 C530,120 420,128 300,128 C180,128 70,132 0,170 L0,162 C70,124 180,120 300,120 C415,120 520,112 552,40 Z" fill="var(--teal)"/>
    </svg>
    <div class="front-brand">
      <div class="brand-name"><span class="brand-dot"></span>TVM8</div>
    </div>
    <div class="social" aria-label="Social links"><span></span><span></span><span></span></div>

    <div class="person-name">Daniel Mercer</div>
    <div class="person-role">Manager</div>

    <div class="contact contact-web">
      <svg viewBox="0 0 16 16"><circle cx="8" cy="8" r="6.5" fill="none" stroke="currentColor" stroke-width="1.4"/><path d="M1.5,8 H14.5 M8,1.5 C4.5,5 4.5,11 8,14.5 C11.5,11 11.5,5 8,1.5" fill="none" stroke="currentColor" stroke-width="1.2"/></svg>
      www.tvm8.com
    </div>
    <div class="contact contact-mail">
      <svg viewBox="0 0 16 16"><rect x="1.5" y="3.5" width="13" height="9" fill="none" stroke="currentColor" stroke-width="1.4"/><path d="M1.5,3.5 L8,9 L14.5,3.5" fill="none" stroke="currentColor" stroke-width="1.4"/></svg>
      dmercer@tvm8.com
    </div>
    <div class="contact contact-phone">
      <svg viewBox="0 0 16 16"><rect x="4" y="1" width="8" height="14" rx="1.5" fill="none" stroke="currentColor" stroke-width="1.4"/><circle cx="8" cy="12.5" r="0.9" fill="currentColor"/></svg>
      555.014.2288
    </div>
  </section>
</main>
</body>
</html>
```